Educational -After School Tutoring

This is a flyer given out to parents from school inside their weekly flyer This flyer should bring a good first impression and carry information about my Tutoring center ( Brightpath Learning) We like this flyer to represent my Academy and the programs that we offer. Also, the flyer should tell how we differentiate from other business
Also, it should give a map or location of my business and the contact information

you may able to get more information from my website brightpathlearnga.example

Target Market(s)

Educational Community ( Parents, Teachers, Students )

Industry/Entity Type

Education

Font styles to use
Serif
Script

Requirements
Must have
• A Picture with students infer the message of tutoring
Nice to have
• teacher explaining or student observing

```html
<!DOCTYPE html>
<html lang="en">
<head>
<meta charset="utf-8">
<title>Brightpath Learning – Flyer</title>
<link href="https://fonts.googleapis.com/css2?family=Bebas+Neue&family=Open+Sans:ital,wght@0,400;0,600;0,700;1,400;1,600;1,800&display=swap" rel="stylesheet">
<style>
:root{
  --teal:#27e2b5;
  --teal-deep:#2aa596;
  --navy:#123a4f;
  --navy-dark:#0f3347;
  --slate:#585d70;
  --slate-light:#767b8f;
  --red:#b81f2f;
  --crimson:#b3121f;
  --paper:#ffffff;
  --paper-gray:#f3f3f3;
  --ink:#333a44;
  --ink-soft:#666b73;
  --band-gray:#e4e5e7;
  --stage:#d9d9d9;
}
*{box-sizing:border-box;margin:0;padding:0}
html,body{width:1200px;height:845px;overflow:hidden}
body{background:var(--stage);font-family:"Open Sans",Arial,sans-serif;color:var(--ink);position:relative}
.page{position:absolute;top:42px;width:540px;height:762px;overflow:hidden;box-shadow:0 2px 8px rgba(0,0,0,.18)}
.page--front{left:40px;background:var(--paper)}
.page--back{left:620px;background:var(--paper-gray)}
.abs{position:absolute}
.display{font-family:"Bebas Neue",Impact,sans-serif;letter-spacing:.5px;font-weight:400}

/* front */
.hero-band{left:0;top:83px;width:540px;height:342px;background:var(--teal)}
.hero-photo{left:0;top:30px;width:250px;height:395px;background:linear-gradient(180deg,#eeb98c 0%,#e8a161 45%,#f08a1b 70%,#e5780f 100%);border-radius:110px 110px 0 0}
.title-box{background:var(--navy);color:#fff;font-size:37px;line-height:1;padding:6px 10px 2px}
.title-1{right:28px;top:39px}
.title-2{right:28px;top:83px}
.dedication{left:262px;top:156px;width:272px;font-weight:800;font-style:italic;font-size:17px;line-height:20px;color:#fff;text-transform:uppercase}
.dedication em{color:var(--navy);font-style:italic}
.tagline{left:262px;top:244px;font-size:10px;line-height:13px;color:#fff}
.intro{left:285px;top:283px;width:240px;font-style:italic;font-size:11px;line-height:14px;color:#fff}
.quote{left:0;top:456px;width:540px;text-align:center;font-size:12.5px;line-height:16px;font-weight:700;color:var(--ink)}
.quote i{font-weight:800}
.quote-sub{left:12px;top:474px;width:516px;text-align:center;font-size:9.5px;line-height:12px;color:var(--ink-soft)}
.section-head{font-size:18px;line-height:22px;font-weight:700;color:var(--navy)}
.section-head span{color:var(--teal-deep)}
.about-head{left:20px;top:520px}
.approach-head{left:290px;top:520px}
.body-small{font-size:6.3px;line-height:10px;color:var(--ink-soft);text-align:justify}
.about-text{left:20px;top:546px;width:235px}
.approach-text{left:290px;top:546px;width:232px}
.divider{left:272px;top:526px;width:1px;height:108px;background:var(--teal)}
.enroll{left:0;top:640px;width:355px;height:98px;background:var(--teal);color:#fff;padding:10px 20px}
.enroll h3{font-size:19px;line-height:24px;font-weight:700;letter-spacing:.3px}
.enroll p{font-size:10px;line-height:13px}
.enroll .gap{margin-top:8px}
.brand-panel{left:355px;top:640px;width:185px;height:98px;background:var(--band-gray);display:flex;align-items:center;justify-content:center;gap:7px}
.brand-dot{width:22px;height:22px;border-radius:50%;background:var(--navy);flex:none}
.brand-name{font-size:15px;font-weight:700;color:var(--navy);line-height:1.05}
.site{right:12px;top:744px;font-size:10px;color:var(--ink)}

/* back */
.offer-title{left:34px;top:42px}
.offer-title .title-box{display:table;font-size:36px;padding:4px 6px 0;margin-bottom:2px}
.offer-lead{left:34px;top:168px;width:150px;font-style:italic;font-weight:800;font-size:13px;line-height:19px;color:var(--crimson)}
.photo{background:linear-gradient(160deg,#4d5b5a,#8d9a97 55%,#c7cbc5)}
.photo-1{left:198px;top:42px;width:150px;height:224px}
.photo-2{left:360px;top:209px;width:150px;height:221px;background:linear-gradient(160deg,#f1d9db,#d8a5ab 50%,#7b5a4a)}
.tile{padding:8px 9px;color:#fff;overflow:hidden}
.tile h4{font-size:14px;font-weight:600;line-height:1.2;margin-bottom:4px}
.tile h4 small{display:block;font-size:7.5px;font-weight:700}
.tile p{font-size:5.6px;line-height:8px;margin-bottom:3px}
.tile ul{list-style:none;font-size:5.6px;line-height:8px;padding-left:6px}
.tile-math{left:352px;top:31px;width:166px;height:168px;background:var(--teal)}
.tile-reading{left:23px;top:276px;width:166px;height:162px;background:var(--slate)}
.tile-writing{left:189px;top:276px;width:163px;height:162px;background:var(--slate-light)}
.tile-sat{left:23px;top:438px;width:166px;height:173px;background:var(--teal-deep)}
.tile-sat h4.second{margin-top:4px}
.tile-cs{left:189px;top:438px;width:163px;height:173px;background:var(--red)}
.tile-robot{left:352px;top:438px;width:166px;height:173px;background:var(--navy-dark)}
.closing{left:27px;top:634px;width:310px;font-size:7px;line-height:10.5px;color:var(--ink-soft)}
.closing p+p{margin-top:6px}
.back-brand{left:360px;top:645px;display:flex;align-items:center;gap:8px}
.back-brand .brand-name{font-size:17px}
.contact-row{left:27px;top:728px;width:490px;display:flex;justify-content:space-between;font-size:7px;color:var(--ink-soft)}
.contact-row span{display:flex;align-items:center;gap:5px}
.chip{width:8px;height:8px;background:var(--navy);display:inline-block}
.chip--teal{background:var(--teal-deep)}
</style>
</head>
<body>

<section class="page page--front">
  <div class="abs hero-band"></div>
  <div class="abs hero-photo" role="img" aria-label="Photo of a smiling schoolboy in an orange polo shirt carrying a backpack"></div>
  <div class="abs title-box display title-1">A Place to Enrich</div>
  <div class="abs title-box display title-2">Students' Potentials</div>

  <h2 class="abs dedication">Brightpath Learning is dedicated to <em>our students' success</em> at school and beyond</h2>
  <p class="abs tagline">Students' Success is Our Success!</p>
  <p class="abs intro">Brightpath Learning strives to improve your children's academic achievements and analytical problem solving skills. We believe that stretching a child's mind through critical thinking skills, accelerated academic programs, and exposure to computer programming and robotics at an early age will help them rise to their true potential.</p>

  <p class="abs quote">We Love Teaching <i>"Teaching is the greatest act of optimism"</i> - Dana Whitfield</p>
  <p class="abs quote-sub">Brightpath Learning provides every student with personal guidance. We give students the platform and tools needed to conquer,to build confidence in them, to excel in their goals, and to achieve their dreams</p>

  <h3 class="abs section-head about-head"><span>ABOUT</span> US</h3>
  <p class="abs body-small about-text">Brightpath Learning in Lakeview, Georgia is a private tutoring center which provides group coaching in Math, Reading, SAT Preparation, and Computer Programming for kids. We are proud to offer a curriculum that is truly unique, providing a strong focus on advanced coaching in Math and Reading. We also provide effective coaching for standardized tests like SAT, ITBS, etc. We step away from the regular coaching method and implement effective problem solving techniques and critical thinking skills to help our children achieve stronger academic results.</p>
  <div class="abs divider"></div>
  <h3 class="abs section-head approach-head">OUR <span>APPROACH</span></h3>
  <p class="abs body-small approach-text">Our approach includes comprehensive evaluations done to determine his/her current levels within the subject(s) of interest. Based on the assessment outcome, we will create an individualized program for each child. Our teachers will work with your child and go over any weak areas to cover subject materials. Once we help your student meet or surpass the required skill level the challenges will be replaced by a newfound confidence and love towards learning.</p>

  <div class="abs enroll">
    <h3>ENROLL NOW</h3>
    <p>Come and take the Free Assessment test!</p>
    <p class="gap">410 Maple Grove Rd, Suite 12<br>Lakeview, GA 30099<br>&#9742; 555-010-4477</p>
  </div>
  <div class="abs brand-panel">
    <span class="brand-dot"></span>
    <span class="brand-name">Brightpath<br>Learning</span>
  </div>
  <p class="abs site">brightpathlearnga.example</p>
</section>

<section class="page page--back">
  <div class="abs offer-title">
    <div class="title-box display">Our</div>
    <div class="title-box display">Service</div>
    <div class="title-box display">Offerings</div>
  </div>
  <p class="abs offer-lead">We cater to students' needs in a variety of forms, from group classes to one-on-one tutoring.</p>

  <div class="abs photo photo-1" role="img" aria-label="Photo of a young boy in glasses writing at a chalkboard"></div>
  <div class="abs photo photo-2" role="img" aria-label="Photo of a teacher helping a smiling student at a desk"></div>

  <div class="abs tile tile-math">
    <h4>Mathematics<small>(Georgia Standard of Education)</small></h4>
    <p>Help young learners build the conceptual understanding needed to tackle more complex mathematical challenges.</p>
    <p>Provide rigorous instruction on state standards of excellence. Develop mathematical reasoning through lessons that use real-world problem solving as instruction.</p>
    <p>We teach young learners to solve problems that also require the application of higher-order thinking skills.</p>
    <p>Adopt appropriate type and method of teaching for students at various skill levels.</p>
  </div>

  <div class="abs tile tile-reading">
    <h4>Reading (GSE)</h4>
    <p>Build strong reading comprehension skills with the right balance of informational and literary text from a wide range of genres.</p>
    <p>Promote comprehension skills in emergent readers and provide rigorous instruction on every reading standard in a developmentally appropriate way.</p>
    <p>Provide instructions required to meet higher expectations and teach students to become independent, critical thinkers.</p>
    <p>Focused on improving Language Fluency Phonetic Awareness, Reading Compression, and Vocabulary skills.</p>
  </div>
  <div class="abs tile tile-writing">
    <h4>Writing (GSE)</h4>
    <p>Our writing program helps students organize and articulate their own ideas to become confident, competent writers and thinkers.</p>
    <p>In this program, students will learn all types of writing: Argumentative, Informative, Scientific, and Narrative writing.</p>
    <p>Participants in this program will also learn about writing structure, correct grammar, review writing strategies, and much more.</p>
    <p>We help students learn the techniques to make their work powerful and exciting. The materials used in this program will be aligned to their GSE standards.</p>
  </div>

  <div class="abs tile tile-sat">
    <h4>SAT Preparation</h4>
    <p>Our dedicated teachers are specialized and highly experienced in SAT preparation, nurture students to achieve higher scores to enter into their top choice colleges. "Practice Makes Perfect" We get the kids in to a routine of consistent practice of various concepts required for success in SAT test.</p>
    <h4 class="second">Critical Thinking</h4>
    <p>Our critical thinking courses are specially designed to make kids to use in-depth analysis of evidence to make decisions and communicate their beliefs clearly and accurately. Kids with good critical thinking skills produce better grades and higher test scores. Our fun and easy to learn courses make students analyze deeper which produces deeper understanding of subject.</p>
  </div>
  <div class="abs tile tile-cs">
    <h4>Computer Science</h4>
    <p>Exposing students to computer science in early ages improves their understanding of technology, which makes them not only users of technology but also innovators of next generation technology.</p>
    <p>Brightpath Learning offers computer science training with strong focus on Programming. We provide age appropriate computer science training which includes valuable concepts of computer programming with comprehensive training for a variety of software applications and key areas like:</p>
    <p>Office suite - HTML Web design - Python Programming - Java Programming - Computer Architecture - Mobile App Programming - Fun Programming for young kids</p>
  </div>
  <div class="abs tile tile-robot">
    <h4>Robotics</h4>
    <p>Robots play a major role in space exploration, industry automation, medical research and many other industries. Introducing the basics of robotics to kids widens their understanding of machines and opens new avenues for creativity and innovation.</p>
    <p>Robot building offers students a platform for learning areas about science, technology, engineering and math (STEM). Students learn how science and engineering principles work together to solve real world problems.</p>
    <p>We offer following robot building classes for all age groups:</p>
    <ul><li>• Starter Build Kits</li><li>• Arena Bots</li></ul>
  </div>

  <div class="abs closing">
    <p>We offer individually tailored courses to meet varying needs of students, whether it is a one-on-one tutoring or special subject tutoring; Brightpath Learning has experienced teachers to help you in any academic subject.</p>
    <p>Brightpath Learning will be able to provide the service you need to "Excel your Goals and Achieve". Do you have different need other than our standard offerings? Please contact us we will customize our offerings to meet your need.</p>
  </div>
  <div class="abs back-brand">
    <span class="brand-dot"></span>
    <span class="brand-name">Brightpath<br>Learning</span>
  </div>

  <div class="abs contact-row">
    <span>
      <svg width="9" height="9" viewBox="0 0 10 10" aria-hidden="true"><rect width="10" height="10" fill="#2aa596"/><path d="M3 2.2l1 1.6-.6.7c.4.9 1.1 1.6 2 2l.7-.6 1.6 1-.5 1.1C4.8 7.8 2.2 5.2 2 2.7z" fill="#fff"/></svg>
      555-010-4477</span>
    <span><i class="chip chip--teal"></i>hello@brightpathlearnga.example</span>
    <span><i class="chip"></i>@brightpath_learn</span>
    <span><i class="chip"></i>/brightpathlearn</span>
    <span><i class="chip"></i>brightpathlearnga.example</span>
  </div>
</section>

</body>
</html>
```